ZAMO needs a beautiful/corp web page

We are a pump an compressor repair facility in Alberta Canada. We love clean looks. white yellows greens blues. main page should involve conola fields, sun shine

Reason: i will be guaranteeing the project keep up the good work

Requirements
Must have
• open conola fields

```html
<!DOCTYPE html>
<html lang="en">
<head>
<meta charset="utf-8">
<title>ZAMO Rotating Solutions</title>
<link rel="stylesheet" href="https://fonts.googleapis.com/css2?family=Montserrat:wght@400;600;700;800&family=Arimo:wght@400;700&display=swap">
<style>
:root{
  --green:#7a9300;
  --orange:#f6a800;
  --field:#e8c20a;
  --field-deep:#d9b000;
  --ink:#231f20;
  --text:#5f5f5f;
  --footer:#262223;
  --white:#ffffff;
  --rule:#c9c9c9;
}
*{margin:0;padding:0;box-sizing:border-box}
html,body{width:1200px;height:836px;overflow:hidden}
body{background:var(--green);font-family:"Arimo",Arial,sans-serif}
.page{position:absolute;left:185px;top:0;width:831px;height:836px;background:var(--white)}

.hero{position:relative;height:453px;overflow:hidden}
.hero-photo{position:absolute;inset:0;background:linear-gradient(180deg,var(--field) 0%,var(--field-deep) 100%)}
.brand{position:absolute;left:36px;top:80px;display:flex;align-items:center;gap:8px}
.brand-dot{width:14px;height:14px;border-radius:50%;background:var(--ink)}
.brand-name{font-family:"Montserrat",sans-serif;font-weight:800;font-size:34px;color:var(--ink);letter-spacing:1px;line-height:1}
.brand-sub{position:absolute;left:36px;top:124px;font-family:"Montserrat",sans-serif;font-size:11px;color:var(--ink)}

.main-nav{position:absolute;left:272px;top:64px;width:559px;height:33px;background:var(--orange);
  display:flex;align-items:center;justify-content:space-around;padding:0 6px}
.main-nav a{font-family:"Montserrat",sans-serif;font-weight:600;font-size:12px;color:var(--white);text-decoration:none}
.main-nav .sep{width:1px;height:9px;background:#9b6a00}

.hero-copy{position:absolute;left:0;right:0;top:198px;text-align:center}
.hero-title{font-family:"Montserrat",sans-serif;font-weight:800;font-size:33px;line-height:41px;color:var(--white);
  text-shadow:0 1px 3px rgba(0,0,0,.45)}
.hero-lead{margin:16px auto 0;width:440px;font-size:12px;line-height:16px;color:var(--ink)}
.hero-btn{display:inline-block;margin-top:24px;width:113px;height:33px;border:2px solid var(--white);
  font-size:12px;line-height:29px;color:var(--ink)}

.intro{position:relative;height:267px}
.intro-photo{position:absolute;left:17px;top:20px;width:159px;height:212px;background:var(--field)}
.welcome{position:absolute;left:198px;top:22px;width:356px}
h2{font-family:"Montserrat",sans-serif;font-weight:600;font-size:24px;color:var(--ink);line-height:1.2}
h2 span{color:var(--orange)}
.welcome p{margin-top:12px;font-size:11px;line-height:18px;color:var(--text)}
.welcome p+p{margin-top:18px}
.more{display:inline-flex;align-items:center;gap:8px;margin-top:14px;font-family:"Montserrat",sans-serif;
  font-weight:700;font-size:11.5px;color:var(--ink);text-decoration:none}
.services{position:absolute;left:577px;top:22px;width:232px}
.services ul{list-style:none;margin-top:10px}
.services li{display:flex;align-items:center;gap:12px;height:31px;padding-left:10px;font-size:11.5px;color:var(--text)}
.services li span{flex:1;border-bottom:1px dashed var(--rule);line-height:30px}

.site-footer{position:relative;height:116px;background:var(--footer);color:var(--white)}
.site-footer h3{position:absolute;left:29px;top:18px;font-family:"Montserrat",sans-serif;font-weight:700;font-size:14px}
.site-footer h3 span{color:var(--orange)}
.addr,.lines{position:absolute;top:46px;font-size:9.5px;line-height:12px}
.addr{left:29px}.lines{left:180px}
.lines a{color:var(--orange);text-decoration:none}
.social{position:absolute;right:26px;top:37px;display:flex;gap:7px}
.social span{width:26px;height:26px;background:var(--orange)}
.copy{position:absolute;right:26px;top:78px;font-size:9.5px}
</style>
</head>
<body>
<div class="page">
  <header class="hero">
    <div class="hero-photo" role="img" aria-label="Photo: open canola field in yellow bloom under a sunny blue sky"></div>
    <div class="brand"><div class="brand-dot"></div><div class="brand-name">ZAMO</div></div>
    <div class="brand-sub">ROTATING SOLUTIONS</div>
    <nav class="main-nav">
      <a href="#">HOME</a><i class="sep"></i>
      <a href="#">ABOUT US</a><i class="sep"></i>
      <a href="#">OUR SERVICES</a><i class="sep"></i>
      <a href="#">OUR PRODUCTS</a><i class="sep"></i>
      <a href="#">CONTACT US</a>
    </nav>
    <div class="hero-copy">
      <h1 class="hero-title">OFFERS A VARIETY OF OPTIONS<br>FOR YOUR ROTATING SOLUTIONS</h1>
      <p class="hero-lead">We are a service provider and process equipment supplier of pump products and customized compressor systems.</p>
      <a class="hero-btn">READ MORE</a>
    </div>
  </header>

  <main class="intro">
    <div class="intro-photo" role="img" aria-label="Photo: canola field stretching to the horizon"></div>
    <section class="welcome">
      <h2>Welcome to <span>Zamo</span></h2>
      <p>Proin gravida nibh vel velit auctor aliquet. Aenean sollicitudin, lorem quis bibendum auctor, nisi elit consequat ipsum, nec sagittis sem nibh id elit. Duis sed odio sit amet nibh vulputate cursus a sit amet mauris. Morbi accumsan ipsum velit. Nam nec tellus a odio tincidunt auctor a</p>
      <p>Ornare odio. Sed non mauris vitae erat consequat auctor eu in elit. per inceptos himenaeos. Mauris in erat justo. Nullam ac urna eu felis</p>
      <a class="more" href="#">READ MORE
        <svg width="7" height="10" viewBox="0 0 7 10"><path d="M1 1l4 4-4 4" fill="none" stroke="#f6a800" stroke-width="2"/></svg></a>
    </section>
    <section class="services">
      <h2>Our <span>Service</span></h2>
      <ul>
        <li><svg width="7" height="10" viewBox="0 0 7 10"><path d="M1 1l4 4-4 4" fill="none" stroke="#f6a800" stroke-width="2"/></svg><span>Proin gravida nibh vel velit auctor</span></li>
        <li><svg width="7" height="10" viewBox="0 0 7 10"><path d="M1 1l4 4-4 4" fill="none" stroke="#f6a800" stroke-width="2"/></svg><span>Aliquet. Aenean sollicitudin, lorem</span></li>
        <li><svg width="7" height="10" viewBox="0 0 7 10"><path d="M1 1l4 4-4 4" fill="none" stroke="#f6a800" stroke-width="2"/></svg><span>Quis bibendum auctor, nisi elit</span></li>
        <li><svg width="7" height="10" viewBox="0 0 7 10"><path d="M1 1l4 4-4 4" fill="none" stroke="#f6a800" stroke-width="2"/></svg><span>Consequat ipsum, nec sagittis sem</span></li>
        <li><svg width="7" height="10" viewBox="0 0 7 10"><path d="M1 1l4 4-4 4" fill="none" stroke="#f6a800" stroke-width="2"/></svg><span>Nibh id elituis sed odio sit amet nibh</span></li>
      </ul>
    </section>
  </main>

  <footer class="site-footer">
    <h3>CONTACT <span>US</span></h3>
    <p class="addr">Lorem Ipsum Stree, Block 234<br>Nam Tellus, 1234, TA,<br>Country , USA</p>
    <p class="lines">P: 1800-555010<br>F: 1023-555018<br>E: <a href="#">hello@zamo-pumps.ca</a></p>
    <div class="social"><span aria-label="Social link"></span><span aria-label="Social link"></span></div>
    <p class="copy">Copyright © 2013 Zamo Rotating Solution, All Rights Reserved</p>
  </footer>
</div>
</body>
</html>
```